Dorvelan Swimming & Athletics Center

We need Business Card for a Athletics center
The logo frome the Uploaded Files ( b card fimal)
Οn one side of card we need the logo of company the Contact and the website:
1. Address:(Limassol, Cyprus 12-14 Stavrinelou str,Ano Trimeni,P.C. 4832)

2.Phone number: (+357) 25-704263

3. Mail: info@dorvelanfit.example

3. Website: www.dorvelanfit.example

Οn the other side of the card we need to write the sport of the company:

1. Artistic Gymnastics
2. Swimming
3. Gym - Fitness
4. Programs
5. Dancing
5.Tennis

From the Uploaded Files you can get the logo.In a logo is behind the black color which can be removed from logo.

Υou can use that color you want.
.
Updates

Industry/Entity Type

Business

Font styles to use
Decorative

Colors
0555a3
ffcf3e
3176b5
0692cd
add136
f04a50
000000
cfcfcf
9d9d9d

Requirements
Should not have
• photos with faces
• photo fro the Website:www.dorvelanfit.example

```html
<!DOCTYPE html>
<html lang="en">
<head>
<meta charset="UTF-8">
<title>Dorvelan Swimming &amp; Athletics Center – Business Card</title>
<link href="https://fonts.googleapis.com/css2?family=Source+Sans+3:wght@400&display=swap" rel="stylesheet">
<style>
  :root {
    --card-white: #ffffff;
    --ink-black: #000000;
    --ink-grey: #9d9d9d;
    --rule-grey: #cfcfcf;
    --band-blue: #1a90d0;
    --band-blue-deep: #0f7fc2;
    --band-blue-light: #2a9ad6;
    --bullet-green: #add136;
    --text-white: #ffffff;
  }
  * { box-sizing: border-box; margin: 0; padding: 0; }
  html, body {
    width: 1200px;
    height: 686px;
    overflow: hidden;
    background: var(--card-white);
  }
  .card {
    position: relative;
    width: 1200px;
    height: 686px;
    background: var(--card-white);
    font-family: "Source Sans 3", "Myriad Pro", Arial, sans-serif;
    font-weight: 400;
  }
  .brand {
    position: absolute;
    left: 265px;
    top: 146px;
    width: 670px;
    height: 135px;
    display: flex;
    align-items: center;
    justify-content: center;
    gap: 30px;
  }
  .brand-name {
    color: var(--ink-black);
    font-size: 76px;
    letter-spacing: 3px;
    line-height: 1;
  }
  .brand-mark {
    width: 84px;
    height: 84px;
    border-radius: 50%;
    border: 3px solid var(--rule-grey);
  }
  .contact {
    position: absolute;
    left: 0;
    top: 318px;
    width: 1200px;
    text-align: center;
    color: var(--ink-grey);
    font-size: 19px;
    line-height: 28px;
  }
  .contact .sep { margin: 0 10px; }
  .sports-band {
    position: absolute;
    left: 0;
    top: 424px;
    width: 1200px;
    height: 262px;
  }
  .band-texture {
    position: absolute;
    inset: 0;
    background: linear-gradient(110deg, var(--band-blue-light) 0%, var(--band-blue) 45%, var(--band-blue-deep) 100%);
  }
  .sports-list {
    position: absolute;
    inset: 0;
    list-style: none;
    display: flex;
    flex-wrap: wrap;
    justify-content: center;
    align-content: flex-start;
    padding: 73px 150px 0;
    row-gap: 10px;
    column-gap: 26px;
  }
  .sport {
    display: flex;
    align-items: center;
    gap: 8px;
    color: var(--text-white);
    font-size: 36px;
    line-height: 42px;
  }
  .sport::before {
    content: "";
    width: 16px;
    height: 16px;
    border-radius: 50%;
    background: var(--bullet-green);
    margin-top: -6px;
  }
  .sports-list .row-break { flex-basis: 100%; height: 0; }
</style>
</head>
<body>
  <main class="card">
    <div class="brand" role="img" aria-label="Dorvelan logo placeholder">
      <span class="brand-name">Dorvelan</span>
      <span class="brand-mark"></span>
    </div>
    <address class="contact" style="font-style: normal;">
      <div>12-14 Stavrinelou str, Ano Trimeni, P.C. 4832, Limassol, Cyprus</div>
      <div>(+357) 25-704263<span class="sep">|</span>info@dorvelanfit.example<span class="sep">|</span>www.dorvelanfit.example</div>
    </address>
    <section class="sports-band">
      <div class="band-texture" role="img" aria-label="Blue band with a soft pattern of overlapping diamond shapes"></div>
      <ul class="sports-list">
        <li class="sport">Artistic Gymnastics</li>
        <li class="sport">Swimming</li>
        <li class="sport">GymFitness</li>
        <li class="row-break" aria-hidden="true"></li>
        <li class="sport">Programs</li>
        <li class="sport">Dancing</li>
        <li class="sport">Tennis</li>
      </ul>
    </section>
  </main>
</body>
</html>
```